Vel-Trax.ch is looking for business card letterhead and envelope C5 with WOW effect

We need a strong business card for our company Vel-Trax.ch, logo is available. You want a black or dark background on which the logo Stark r% 26 # 252; appears. Letterhead and envelope in C5 format should be in a similar design, but does not have to be We need a strong business card for our company Vel-Trax.ch, logo is available. A black or dark background is desired, on which the logo Stark comes across. The letterhead and the envelope in C5 format should have a similar design.

Target Market(s)

Private customers as well as entrepreneurs

Contact Information for Business Card

E-mail: info@vel-trax.ch
Web.www.Vel-Trax.ch
Tel: +41 ( 0 ) 79 684 3027
Adresse:
Lindenhaldeweg 14
9418 Brenzikon

Hier kann man Icons verwenden für Email,Tel und Adressse

Font styles to use
Other font styles liked:
• Dubai,bold

Colors

Designer to choose colors to be used in the design.

Requirements
Must have
• WOW effect
Nice to have
• R% 26 # 252; back business card with our service listings. - VEHICLE LABELING - SHOP WINDOW LABELING - STICKERS AND MUCH MORE ... in red color

```html
<!DOCTYPE html>
<html lang="de">
<head>
<meta charset="utf-8">
<title>Vel-Trax.ch – Visitenkarte</title>
<link rel="stylesheet" href="https://fonts.googleapis.com/css2?family=Lato:wght@400;700;900&display=swap">
<style>
  :root {
    --backdrop: #dedede;
    --card-light: #ffffff;
    --card-dark: #070707;
    --accent: #fdc813;
    --text-grey: #8a8a8a;
    --ink: #111111;
    --paper: #ffffff;
  }
  * { margin: 0; padding: 0; box-sizing: border-box; }
  html, body {
    width: 1200px;
    height: 960px;
    overflow: hidden;
    background: var(--backdrop);
    font-family: "Lato", Arial, sans-serif;
  }
  .canvas { position: relative; width: 1200px; height: 960px; }
  .card {
    position: absolute;
    left: 281px;
    width: 655px;
    height: 374px;
    border-radius: 23px;
    overflow: hidden;
  }
  .card--front { top: 80px; background: var(--card-light); }
  .card--back { top: 506px; background: var(--card-dark); }

  .person { position: absolute; left: 68px; top: 64px; }
  .person__name {
    color: var(--accent);
    font-weight: 700;
    font-size: 27px;
    line-height: 1.1;
  }
  .person__role {
    color: var(--text-grey);
    font-size: 18px;
    margin-top: 4px;
  }
  .address {
    position: absolute;
    left: 68px;
    top: 186px;
    color: var(--text-grey);
    font-size: 17.5px;
    line-height: 24px;
    font-style: normal;
  }
  .contact {
    position: absolute;
    left: 68px;
    top: 248px;
    list-style: none;
    color: var(--text-grey);
    font-size: 17.5px;
    line-height: 24px;
  }
  .contact__item { display: flex; align-items: center; gap: 8px; }
  .contact__icon { width: 14px; height: 14px; flex: none; }

  .brand { position: absolute; display: flex; align-items: center; }
  .brand__dot { border-radius: 50%; background: var(--accent); flex: none; }
  .brand__name { font-weight: 900; letter-spacing: 0.5px; }

  .brand--front { left: 370px; top: 232px; gap: 16px; }
  .brand--front .brand__dot { width: 48px; height: 48px; }
  .brand--front .brand__name { color: var(--ink); font-size: 28px; }

  .brand--back {
    left: 0; right: 0; top: 0; bottom: 12px;
    justify-content: center;
    gap: 22px;
  }
  .brand--back .brand__dot { width: 76px; height: 76px; }
  .brand--back .brand__name { color: var(--paper); font-size: 38px; }
</style>
</head>
<body>
<main class="canvas">
  <section class="card card--front" aria-label="Vorderseite">
    <div class="person">
      <p class="person__name">Marco Keller</p>
      <p class="person__role">Managing Director</p>
    </div>
    <address class="address">
      Lindenhaldeweg 14<br>
      9418 Brenzikon
    </address>
    <ul class="contact">
      <li class="contact__item">
        <svg class="contact__icon" viewBox="0 0 14 14" aria-hidden="true">
          <path d="M3 1.5 L5 3.5 L4 5 Q5.5 8 9 10 L10.5 9 L12.5 11 L11 12.8 Q4 11 1.2 3 Z" fill="var(--accent)"/>
        </svg>
        +41 ( 0 ) 79 684 3027
      </li>
      <li class="contact__item">
        <svg class="contact__icon" viewBox="0 0 14 14" aria-hidden="true">
          <rect x="1" y="3" width="12" height="8.5" rx="1" fill="var(--accent)"/>
          <path d="M1.5 3.5 L7 8 L12.5 3.5" fill="none" stroke="var(--card-light)" stroke-width="1.1"/>
        </svg>
        info@vel-trax.ch
      </li>
      <li class="contact__item">
        <svg class="contact__icon" viewBox="0 0 14 14" aria-hidden="true">
          <g fill="none" stroke="var(--accent)" stroke-width="1.1">
            <circle cx="7" cy="7" r="5.8"/>
            <ellipse cx="7" cy="7" rx="2.5" ry="5.8"/>
            <path d="M1.2 7 H12.8 M2 4 H12 M2 10 H12"/>
          </g>
        </svg>
        www.Vel-Trax.ch
      </li>
    </ul>
    <div class="brand brand--front">
      <span class="brand__dot" aria-hidden="true"></span>
      <span class="brand__name">Vel-Trax.ch</span>
    </div>
  </section>

  <section class="card card--back" aria-label="Rückseite">
    <div class="brand brand--back">
      <span class="brand__dot" aria-hidden="true"></span>
      <span class="brand__name">Vel-Trax.ch</span>
    </div>
  </section>
</main>
</body>
</html>
```